New Infographic Design Project

Hi, I have another project to work on if you are interested. It is a horizontal style infographic with 6 steps. It should display the step Number (1-6), Title, and an Icon.

Step 1 - Strong Phone Interview
Step 2 - Pre-Employment
Step 3 - Prep & Do In-Person Interview
Step 4 - Second Interview
Step 5 - Reference Checks
Step 6 - Job Offer

More flexible on colors with this one, but keep it professional.

```html
<!DOCTYPE html>
<html lang="en">
<head>
<meta charset="UTF-8">
<title>6 Steps Hiring Process Infographic</title>
<link rel="stylesheet" href="https://fonts.googleapis.com/css2?family=Montserrat:wght@300;500;600;800&display=swap">
<style>
  :root {
    --backdrop: #4d4d4d;
    --card: #ffffff;
    --heading: #555555;
    --rule: #cfcfcf;
    --dots: #8a8a8a;
    --step-1: #84c35c;
    --step-2: #57a04b;
    --step-3: #4db8c7;
    --step-4: #0088ad;
    --step-5: #4a4594;
    --step-6: #3f2e62;
  }
  * { box-sizing: border-box; margin: 0; padding: 0; }
  html, body {
    width: 1200px; height: 733px; overflow: hidden;
    background: var(--backdrop);
    font-family: "Montserrat", Arial, sans-serif;
  }
  .card {
    position: absolute; left: 41px; top: 42px;
    width: 1117px; height: 648px;
    background: var(--card); border-radius: 20px; overflow: hidden;
  }
  .heading {
    position: absolute; top: 67px; left: 0; width: 100%;
    text-align: center; font-weight: 500; font-size: 29px;
    color: var(--heading); letter-spacing: 0.3px;
  }
  .subheading {
    position: absolute; top: 121px; left: 0; width: 100%;
    text-align: center; font-weight: 300; font-size: 20px;
    color: var(--heading); letter-spacing: 0.5px;
  }
  .rule { position: absolute; top: 133px; height: 1px; background: var(--rule); }
  .rule--left { left: 46px; width: 456px; }
  .rule--right { left: 610px; width: 464px; }
  .timeline { position: absolute; left: 0; top: 0; width: 1117px; height: 648px; }
  .step-icon { position: absolute; top: 203px; width: 96px; height: 96px; border-radius: 50%;
    border: 2px solid currentColor; display: flex; align-items: center; justify-content: center; }
  .step-icon__art { width: 72px; height: 72px; border-radius: 50%; background: currentColor; opacity: 0.22; }
  .step-number {
    position: absolute; top: 402px; width: 120px; text-align: center;
    font-weight: 600; font-size: 29px; letter-spacing: 0.5px;
  }
  .bands { position: absolute; left: 0; top: 391px; width: 1117px; height: 201px; display: flex; }
  .band {
    flex: 1 1 0; height: 100%; color: #fff; text-align: center;
    clip-path: polygon(0 0, calc(50% - 40px) 0, 50% 37px, calc(50% + 40px) 0, 100% 0, 100% 100%, 0 100%);
    padding-top: 70px; font-weight: 800; font-size: 17px; line-height: 27px;
    letter-spacing: 0.6px; text-transform: uppercase;
  }
  .c1 { color: var(--step-1); } .c2 { color: var(--step-2); } .c3 { color: var(--step-3); }
  .c4 { color: var(--step-4); } .c5 { color: var(--step-5); } .c6 { color: var(--step-6); }
  .band.b1 { background: var(--step-1); } .band.b2 { background: var(--step-2); }
  .band.b3 { background: var(--step-3); } .band.b4 { background: var(--step-4); }
  .band.b5 { background: var(--step-5); } .band.b6 { background: var(--step-6); }
</style>
</head>
<body>
<main class="card">
  <h1 class="heading">6 Steps Infographic Design Project</h1>
  <div class="rule rule--left"></div>
  <p class="subheading">(Title)</p>
  <div class="rule rule--right"></div>

  <div class="step-icon c1" style="left:44px"><div class="step-icon__art" role="img" aria-label="Icon: phone handsets with speech bubbles"></div></div>
  <div class="step-icon c2" style="left:231px"><div class="step-icon__art" role="img" aria-label="Icon: person with clipboard checklist and pen"></div></div>
  <div class="step-icon c3" style="left:418px"><div class="step-icon__art" role="img" aria-label="Icon: two people facing each other across a desk"></div></div>
  <div class="step-icon c4" style="left:605px"><div class="step-icon__art" role="img" aria-label="Icon: interviewer and candidate with speech bubble"></div></div>
  <div class="step-icon c5" style="left:791px"><div class="step-icon__art" role="img" aria-label="Icon: profile document with pencil"></div></div>
  <div class="step-icon c6" style="left:977px"><div class="step-icon__art" role="img" aria-label="Icon: handshake under a profile card"></div></div>

  <svg class="timeline" viewBox="0 0 1117 648" aria-hidden="true">
    <line x1="46" y1="328" x2="1078" y2="328" stroke="var(--dots)" stroke-width="2.4" stroke-linecap="round" stroke-dasharray="0 6.2"/>
    <g stroke="#555" stroke-width="1.2">
      <line x1="92" y1="340" x2="92" y2="356"/><line x1="279" y1="340" x2="279" y2="356"/>
      <line x1="466" y1="340" x2="466" y2="356"/><line x1="653" y1="340" x2="653" y2="356"/>
      <line x1="839" y1="340" x2="839" y2="356"/><line x1="1025" y1="340" x2="1025" y2="356"/>
    </g>
    <g fill="#fff" stroke="#555" stroke-width="1.2">
      <circle cx="92" cy="328" r="6"/><circle cx="279" cy="328" r="6"/><circle cx="466" cy="328" r="6"/>
      <circle cx="653" cy="328" r="6"/><circle cx="839" cy="328" r="6"/><circle cx="1025" cy="328" r="6"/>
    </g>
    <circle cx="92" cy="328" r="3.4" fill="var(--step-1)"/>
    <circle cx="279" cy="328" r="3.4" fill="var(--step-2)"/>
    <circle cx="466" cy="328" r="3.4" fill="var(--step-3)"/>
    <circle cx="653" cy="328" r="3.4" fill="var(--step-4)"/>
    <circle cx="839" cy="328" r="3.4" fill="var(--step-5)"/>
    <circle cx="1025" cy="328" r="3.4" fill="var(--step-6)"/>
  </svg>

  <div class="step-number c1" style="left:32px;top:361px">01</div>
  <div class="step-number c2" style="left:219px;top:361px">02</div>
  <div class="step-number c3" style="left:406px;top:361px">03</div>
  <div class="step-number c4" style="left:593px;top:361px">04</div>
  <div class="step-number c5" style="left:779px;top:361px">05</div>
  <div class="step-number c6" style="left:965px;top:361px">06</div>

  <section class="bands">
    <div class="band b1">Strong<br>Phone<br>Interview</div>
    <div class="band b2">Pre-<br>Employment</div>
    <div class="band b3">Pre-Do In<br>Person<br>Interview</div>
    <div class="band b4">Second<br>Interview</div>
    <div class="band b5">Reference<br>Checks</div>
    <div class="band b6">Job<br>Offer</div>
  </section>
</main>
</body>
</html>
```